Miriams Professional Resume

Pls upgrade to make look more effective and perhaps add α photo on it, both options with photo and without would be great. Thanks very much. I would also like the resume so I can edit as well if I need to down the track.

Target Market(s)

This is my professional resume to make it more effective to potential senior hiring managers,

Colors
f04a50

Requirements
Must have
• Professional look.

```html
<!DOCTYPE html>
<html lang="en">
<head>
<meta charset="utf-8">
<title>Miriam Hale – Resume</title>
<link href="https://fonts.googleapis.com/css2?family=Bebas+Neue&family=Barlow+Semi+Condensed:wght@600&family=Montserrat:wght@400;700&family=Source+Sans+3:wght@400;600&display=swap" rel="stylesheet">
<style>
:root{
  --red:#f04a50;
  --grey:#8c8c8c;
  --bg:#5f5f5f;
  --ink:#2b2b2b;
  --white:#fff;
  --line:#9a9a9a;
}
*{box-sizing:border-box;margin:0;padding:0}
html,body{width:1200px;height:1200px;overflow:hidden;background:var(--bg)}
body{position:relative;font-family:"Source Sans 3",sans-serif;color:var(--ink)}
.page{position:absolute;top:251px;width:532px;height:752px;background:var(--white)}
.page--one{left:49px}
.page--two{left:620px}

/* sidebar */
.sidebar{position:absolute;left:0;top:0;width:197px;height:100%;background:var(--red);color:var(--white)}
.portrait{position:absolute;left:25px;top:24px;width:150px;height:150px;border-radius:50%;border:4px solid var(--white);background:radial-gradient(circle at 50% 40%,#e9dedb 0%,#d2b8b4 45%,#b44f5a 100%)}
.name{position:absolute;left:0;width:197px;top:196px;text-align:center;font-family:"Bebas Neue",sans-serif;font-weight:400;font-size:33px;letter-spacing:.3px;line-height:1}
.role{position:absolute;left:24px;width:160px;top:236px;font-weight:600;font-size:10.4px;line-height:12.3px}
.email{position:absolute;left:24px;top:296px;font-size:7.4px;display:flex;align-items:center;gap:6px}
.rule{position:absolute;left:24px;width:150px;height:1px;background:rgba(255,255,255,.8)}
.tags{position:absolute;left:24px;top:346px;width:160px;font-weight:600;font-size:8.8px;line-height:10.8px}
.about{position:absolute;left:24px;top:391px;width:148px;font-size:7.6px;line-height:10.2px;text-align:justify}
.about p{margin-bottom:10px}
.profile{position:absolute;left:24px;top:666px;font-size:10.4px;line-height:13px}
.profile strong{font-weight:600}

/* headers */
.band{position:absolute;background:var(--grey);color:var(--white);font-family:"Barlow Semi Condensed",sans-serif;font-weight:600;text-align:center;font-size:16px;letter-spacing:.3px;display:flex;align-items:center;justify-content:center}
.jobhead{position:absolute;background:var(--red);color:var(--white);text-align:center;font-family:"Montserrat",sans-serif;font-size:9.2px;line-height:11.8px;display:flex;flex-direction:column;justify-content:center;padding:0 4px}
.jobhead b{font-weight:700}
.jobhead--narrow{font-size:8.6px;line-height:11.6px}

/* tables */
.grid{position:absolute;border-collapse:collapse;font-size:7.4px;line-height:9.4px}
.grid td{border:1px solid var(--line);padding:3px 5px;vertical-align:top}
.grid b{font-weight:600}

/* ticked lists */
.ticks{position:absolute;list-style:none;font-size:7.9px;line-height:10.2px;text-align:justify}
.ticks li{position:relative;padding-left:10px;margin-bottom:5.9px}
.ticks li::before{content:"";position:absolute;left:0;top:2.5px;width:4.5px;height:4.5px;border:1px solid var(--red)}
.ticks li::after{content:"";position:absolute;left:2px;top:1.5px;width:2.2px;height:4px;border-right:1.2px solid var(--red);border-bottom:1.2px solid var(--red);transform:rotate(40deg)}

.footer{position:absolute;left:0;bottom:0;width:100%;height:50px;background:var(--red);color:var(--white);text-align:center;font-size:10.4px;line-height:12.5px;padding-top:7px}
.footer strong{font-weight:600}
</style>
</head>
<body>

<section class="page page--one">
  <aside class="sidebar">
    <div class="portrait" role="img" aria-label="Portrait photo of Miriam Hale"></div>
    <h1 class="name">MIRIAM HALE</h1>
    <p class="role">Senior Manager, Organisational Development Director with 15 + years’ experience Singapore, 508214</p>
    <p class="email">
      <svg width="11" height="8" viewBox="0 0 11 8"><rect x=".5" y=".5" width="10" height="7" fill="none" stroke="#fff"/><path d="M.5 .5 5.5 4.5 10.5 .5" fill="none" stroke="#fff"/></svg>
      miriamh@halebusinessconsulting.com
    </p>
    <div class="rule" style="top:325px"></div>
    <p class="tags"># HR Strategy # HR Daily Operations<br># HR Projects # Talent Management<br># Business Solutions.</p>
    <div class="about">
      <p>My strength is in leadership, developing strategies and providing excellence in HR Operational Services, Recruiting, People Development and building high performing teams to accelerate business performance and drive engagement.</p>
      <p>Masters in Strategic Organisational Development. As an authentic leader I excel at navigating across the business to build a positive culture while consulting with executives to understand imperative business needs and recommend the best solution.</p>
      <p>Successfully rolled out Fizzco Project for 200 + new customer sites for the NOVA Perfect Fruit Project and actively recruited for 20 + technical field service agents, developed their capabilities and achieved 100 % completion of the project.</p>
    </div>
    <div class="rule" style="top:629px"></div>
    <p class="profile"><strong>Online Profile:</strong><br>https://www.profilehub.com/in/<br>miriam-hale-4b7c00215</p>
  </aside>

  <h2 class="band" style="left:214px;top:24px;width:293px;height:32px">SKILLS</h2>
  <table class="grid" style="left:214px;top:59px;width:293px">
    <tr><td style="width:143px;height:22px">Human Resources Strategy</td><td>HR Policy</td></tr>
    <tr><td style="height:21px">Human Resources Operations</td><td>Consulting, Stakeholder Management</td></tr>
    <tr><td style="height:31px">Recruitment Process, Talent Acquisition</td><td>Talent Management, Performance Management, Competency Development.</td></tr>
    <tr><td style="height:31px">Singapore, Employment Legislation &amp; Industrial Relations.</td><td>Australia, Fair Work, National Standards and Awards.</td></tr>
    <tr><td style="height:22px">HR Business Partner</td><td>HR Project Management</td></tr>
  </table>

  <h2 class="band" style="left:214px;top:195px;width:293px;height:33px">WORK EXPERIENCE</h2>
  <div class="jobhead" style="left:214px;top:231px;width:293px;height:73px">
    <b>Senior Manager, Organisational Development Director, Service, FMCG Industry</b>
    <span>Hale Business Consulting Singapore</span>
    <span>August 2015 to Present</span>
  </div>

  <ul class="ticks" style="left:216px;top:317px;width:291px">
    <li>Delivered HR Strategy and Daily HR Operations, HR Policy, Recruitment, Performance Management and Communications.</li>
    <li>Leadership, Team Management to 20 + Technical Field Service Agents, FMCG/ F &amp; B Retail Project.</li>
    <li>Recruitment Process for MNCs – Fizzco, Crispy Hen and Pride Brewing for large scale projects.</li>
    <li>HR Advisor to business leaders to achieve business strategic objectives.</li>
    <li>Worked with Senior Leaders in manpower planning, skill development and tracking.</li>
    <li>Developed action plans and strategies to support business needs, talent management, performance management check ins.</li>
    <li>HRBP, Stakeholder Management, Workforce Planning for NOVA Project Roll Out.</li>
    <li>Project P + L Financial Management to $ 1.2 Million SG</li>
    <li>Digitalised business solution of online Service App, digitalised all services improvements to value add, increase efficiencies, transparency and reporting to customers.</li>
    <li>Provide tools required for Team Members and training on new Service App system.</li>
    <li>Manage Performance Management Process check ins, which resulted in greater levels of engagement</li>
    <li>Identify, source, interview, select the right talent to service 200 equipment assets/per month ie. 400 + field services performed each month and efficient operational call outs.</li>
    <li>Oversee weekly payroll and summary report. Sign off on PAYG Tax and GST Report</li>
    <li>Educated new hires on expected job tasks, compensation and benefits to set clear expectations.</li>
    <li>Coaching on expected behaviours through consultations, job spec and code of business reference.</li>
    <li>Project Management - resourcing and operational requirements regards to the roll out of Fizzco and Crispy Hen Technical Field Services for 200 equipment machines assets per month to deliver positive customer service results.</li>
  </ul>
</section>

<section class="page page--two">
  <div class="jobhead" style="left:24px;top:25px;width:228px;height:51px">
    <b>Brightcore Pty. Ltd, Organisational Development Director, Client Relations.</b>
    <span>Australia, June 2008 to August 2015</span>
  </div>
  <div class="jobhead jobhead--narrow" style="left:278px;top:25px;width:228px;height:51px">
    <b>Wexley College, Director Career Services.</b>
    <span>USA, October 2003 to December 2007</span>
  </div>

  <ul class="ticks" style="left:25px;top:86px;width:228px">
    <li>Established Business Strategy in consultation with management.</li>
    <li>Delivered HR Strategy and daily hands on Human Resources Operations: Recruitment,Performance Management and Training and Development.</li>
    <li>Leadership to Team of 20 + resources, created a high performing service focused team.</li>
    <li>Client relations, effective communications and stakeholder management.</li>
    <li>Managed recruitment process for Equipment Field Services Team for Multi National Client Projects: Fizzco, Crispy Hen and Pride Brewing.</li>
    <li>Recruit new Service Provider contracts with Fizzco, Crispy Hen, Burger Lane and PRIDE.</li>
    <li>Project P + L Financial Management to $ 1.2m SG</li>
    <li>Workforce Planning on Technical Field Projects for Fizzco and Crispy Hen for resources across NSW, QLD, VIC and SA for &gt; 200 services equipment assets, 400 + operational field services performed per month.</li>
    <li>Focused on quality service results, delivering a positive customer service experience.</li>
  </ul>
  <ul class="ticks" style="left:279px;top:86px;width:228px">
    <li>Brand expansion, Business Development, Marketing of Wexley College into San Francisco, Sacramento, Fremont, Santa Clara and the Bay Area.</li>
    <li>Built out the department from scratch, developed strategies, process and service standards.</li>
    <li>HR Strategy and Human Resource Operations: Recruitment, Job Placement, Performance Management, HR Policy, Training and Development.</li>
    <li>Graduate Program Placement for 700 + Medical graduates, MA, LVN and RN Program.</li>
    <li>Acquired new accounts from multiple hospitals and medical centres across the San Francisco Bay Area.</li>
    <li>Project Management with Senior Leadership Team for Board of Private Education Accreditation Business Goal, engagement and contracts for preceptorships sites to facilitate L &amp; D.</li>
    <li>Awarded 2005 - Employee of the Year</li>
    <li>Account Management: Redwood Health, Oakridge Medical Centre, Valley Medical Centre and Harbor Veterans Network.</li>
  </ul>

  <div class="jobhead" style="left:23px;top:356px;width:483px;height:36px"><b>Recruitment Consultant, Harlow International, Health Care and IT Industry</b><span>Australia, July 2002 to April 2003</span></div>
  <div class="jobhead" style="left:23px;top:396px;width:483px;height:36px"><b>Recruitment Consultant, Netvance, IT Industry</b><span>Australia, July 2001 to May 2002</span></div>
  <div class="jobhead" style="left:23px;top:436px;width:483px;height:36px"><b>Sales and IT Sourcer, Corlink Systems, IT Industry</b><span>Australia, April 2000 to April 2001</span></div>

  <h2 class="band" style="left:23px;top:479px;width:483px;height:32px">EDUCATION</h2>
  <table class="grid" style="left:23px;top:513px;width:483px">
    <tr>
      <td style="width:162px;height:62px"><b>Masters in Strategic Organisational Development</b><br>Northern Ranges University, Australia<br>December 2011 to December 2017</td>
      <td style="width:167px"><b>Management in Human Resources Certificate – Graduated with Distinction</b><br>Pacific Coast University Extension Program, USA<br>June 2003 – November 2006</td>
      <td><b>Bachelor of Business in Tourism Management</b><br>Eastern Shore University, Australia<br>January 1992 to December 1996</td>
    </tr>
  </table>

  <h2 class="band" style="left:23px;top:581px;width:483px;height:32px">PROFESSIONAL MEMBERSHIPS</h2>
  <table class="grid" style="left:23px;top:615px;width:483px">
    <tr><td style="width:240px;height:22px;padding-top:6px">Member of Singapore People Practice Institute, 104 2871 2020</td><td style="padding-top:6px">Member of Australian People Practice Institute, 362518.</td></tr>
  </table>

  <h2 class="band" style="left:23px;top:642px;width:483px;height:32px">CURRENT COURSES COMPLETED, 2020</h2>
  <table class="grid" style="left:23px;top:676px;width:483px">
    <tr><td style="width:264px;height:22px;padding-top:6px">Singapore Employment Legislation and Industrial Relations, SPPI, 2020.</td><td style="padding-top:6px">Human Resource Analytics and Insights, SPPI, 2020.</td></tr>
  </table>

  <footer class="footer"><strong>Online Profile:</strong><br>https://www.profilehub.com/in/miriam-hale-4b7c00215</footer>
</section>

</body>
</html>
```